Self Storage Company Needs Postcard Design & Flyer Needed

The name of our company is Tall Pine Lockers. We are going to be opening two brand new locations. I need a postcard designed that we will mail to several thousand addresses near our new locations. The postcard needs to announce the opening of our new locations and our special promotion.
I need to have a postcard design that is catchy and worded in a way that will get people to stop by the stores and when they do they will select a key and if that key opens the lock then they will win 3 months of free storage.
1. NOW OPEN! UNLOCK FREE RENT TODAY.
2. Stop by one of our brand new locations and test your luck. Draw a key and if it opens the lock you win three months of free storage.
3. Hurry in, limited time only.
4. These locations need to be listed on postcard:
Tall Pine Lockers
24815 Harrowgate Lane
Noblesville, IN 46062
317.555.0143
Tall Pine Lockers
16250 Quillon Meadow Drive
Fishers, IN 46038
317-555-0178
5. website address: www.tallpinelockers.example
6. logo attached.
7. feel free to use any snapvault photos
8. I've attached a flyer that has amenities listed. Feel free to use as many as them as you would like.
I also need to have a 8.5" X 11" flyer designed to match the postcards that we will display in the offices.
Look and feel
Each slider illustrates characteristics of the customer's brand and the style your logo design should communicate.

```html
<!DOCTYPE html>
<html lang="en">
<head>
<meta charset="utf-8">
<title>Tall Pine Lockers – Now Open Flyer</title>
<link rel="stylesheet" href="https://fonts.googleapis.com/css2?family=Oswald:wght@400;500&family=Lato:wght@400;700&family=Raleway:wght@300&display=swap">
<style>
  :root{
    --stage:#e4e4e4;
    --paper:#ffffff;
    --crimson:#d41f48;
    --sun:#f8ea2a;
    --ink:#222222;
    --slate:#7d7a7b;
    --photo-warm-a:#d9c3a5;
    --photo-warm-b:#eef0f3;
    --photo-cool-a:#c9cfd8;
    --photo-cool-b:#e7d3b6;
  }
  *{box-sizing:border-box;margin:0;padding:0}
  html,body{width:1200px;height:1200px;overflow:hidden;background:var(--stage)}
  .flyer{position:absolute;left:175px;top:50px;width:850px;height:1100px;background:var(--paper);overflow:hidden;box-shadow:0 10px 30px rgba(0,0,0,.18);font-family:"Lato",sans-serif;color:var(--ink)}
  .flyer__shapes{position:absolute;inset:0}
  .brand-name{position:absolute;left:36px;top:34px;display:flex;align-items:center;gap:10px;font-family:"Lato",sans-serif;font-weight:700;font-size:26px;color:var(--crimson)}
  .brand-name__mark{width:18px;height:18px;background:var(--sun)}
  .tagline{position:absolute;right:22px;top:244px;width:300px;text-align:right;font-family:"Oswald",sans-serif;font-weight:400;font-size:30px;line-height:36px;color:#fff}
  .open-badge{position:absolute;left:320px;top:210px;width:190px;height:190px;border-radius:50%;background:var(--sun);box-shadow:0 0 0 6px rgba(248,234,42,.45);display:flex;align-items:center;justify-content:center;text-align:center;font-family:"Oswald",sans-serif;font-weight:500;font-size:24px;line-height:30px;color:var(--ink)}
  .amenities__title{position:absolute;left:430px;top:462px;font-family:"Raleway",sans-serif;font-weight:300;font-size:40px;color:var(--crimson);padding-bottom:4px;border-bottom:1px solid var(--crimson)}
  .amenities__list{position:absolute;list-style:none;font-size:14px;line-height:19px}
  .amenities__list li::before{content:"•";margin-right:7px}
  .amenities__list--main{left:370px;top:560px}
  .amenities__list--supplies{left:640px;top:545px;font-size:13px;line-height:18px}
  .hurry{position:absolute;left:470px;top:770px;width:340px;height:96px;border-radius:20px;background:var(--crimson);color:#fff;display:flex;align-items:center;justify-content:center;text-align:center;font-family:"Lato",sans-serif;font-weight:700;font-size:30px;line-height:36px}
  .locations__name{position:absolute;left:0;right:0;top:884px;text-align:center;font-family:"Lato",sans-serif;font-weight:700;font-size:22px;color:var(--crimson)}
  .location{position:absolute;top:920px;display:flex;gap:10px;font-size:14px;line-height:18px;color:var(--ink)}
  .location--noblesville{left:170px}
  .location--fishers{left:470px}
  .location__icons{display:flex;flex-direction:column;gap:18px;padding-top:2px}
  .location__icons svg{width:16px;height:16px;display:block}
</style>
</head>
<body>
<main class="flyer">
  <svg class="flyer__shapes" width="850" height="1100" viewBox="0 0 850 1100">
    <defs>
      <linearGradient id="moversPhoto" x1="0" y1="0" x2="1" y2="1">
        <stop offset="0" stop-color="var(--photo-cool-a)"/><stop offset="1" stop-color="var(--photo-warm-b)"/>
      </linearGradient>
      <linearGradient id="workerPhoto" x1="0" y1="0" x2="1" y2="1">
        <stop offset="0" stop-color="var(--photo-cool-b)"/><stop offset="1" stop-color="var(--photo-warm-a)"/>
      </linearGradient>
      <linearGradient id="suppliesPhoto" x1="0" y1="0" x2="1" y2="1">
        <stop offset="0" stop-color="#e8dccb"/><stop offset="1" stop-color="#c9a77c"/>
      </linearGradient>
    </defs>
    <rect role="img" aria-label="Photo of a couple carrying moving boxes into a bright room" x="0" y="0" width="850" height="300" fill="url(#moversPhoto)"/>
    <polygon role="img" aria-label="Photo of a mover in a hard hat carrying a cardboard box" points="0,306 470,306 470,466 0,560" fill="url(#workerPhoto)"/>
    <rect x="0" y="300" width="470" height="6" fill="var(--crimson)"/>
    <polygon points="0,560 850,390 850,1100 0,1100" fill="var(--paper)"/>
    <polygon points="850,30 850,390 400,480" fill="var(--crimson)"/>
    <rect role="img" aria-label="Photo of stacked cardboard boxes, a red hand truck and packing supplies" x="40" y="630" width="310" height="240" rx="4" fill="url(#suppliesPhoto)"/>
    <line x1="0" y1="992" x2="850" y2="992" stroke="var(--crimson)" stroke-width="2"/>
    <rect x="0" y="1000" width="850" height="100" fill="var(--slate)"/>
    <line x1="0" y1="1070" x2="850" y2="1070" stroke="var(--crimson)" stroke-width="2"/>
  </svg>

  <div class="brand-name"><span class="brand-name__mark"></span>Tall Pine Lockers</div>
  <p class="tagline">Friendly<br>Storage Experts,<br>Now in Your<br>Neighborhood</p>
  <p class="open-badge">NOW OPEN!<br>UNLOCK FREE<br>RENT TODAY</p>

  <h2 class="amenities__title">Amenities</h2>
  <ul class="amenities__list amenities__list--main">
    <li>Months-to-Month Leases</li>
    <li>Online Payments</li>
    <li>Gated Property Access</li>
    <li>24-Hour Video Monitoring</li>
    <li>Climate Control Available</li>
    <li>24-Hour Coded Access Available</li>
    <li>Convenient Loading Areas</li>
    <li>Discounted Pre-Pay Program</li>
    <li>Tenant Referral Rewards</li>
    <li>Available Carts and Dollies</li>
    <li>Small, Medium &amp; Large Boxes</li>
  </ul>
  <ul class="amenities__list amenities__list--supplies">
    <li>Specialty Boxes</li>
    <li>2" Disc &amp; Cylinder Locks</li>
    <li>Furniture Covers</li>
    <li>Foam Packing Peanuts</li>
    <li>Bubble Wrap</li>
    <li>Stretch Cords</li>
    <li>Nylon Rope</li>
    <li>Moving Blankets</li>
    <li>Tap and Tap Gun</li>
    <li>And much, much more....</li>
  </ul>

  <p class="hurry">Hurry In!<br>Limited Time Only</p>

  <h3 class="locations__name">Tall Pine Lockers</h3>
  <div class="location location--noblesville">
    <div class="location__icons">
      <svg viewBox="0 0 16 16"><path d="M8 1a5 5 0 0 0-5 5c0 4 5 9 5 9s5-5 5-9a5 5 0 0 0-5-5z" fill="var(--crimson)"/><circle cx="8" cy="6" r="2" fill="#fff"/></svg>
      <svg viewBox="0 0 16 16"><circle cx="8" cy="8" r="8" fill="var(--crimson)"/><path d="M5 4l2 2-1 1.2c.6 1.2 1.6 2.2 2.8 2.8L10 9l2 2-1.2 1.4C7.5 12 4 8.5 3.6 5.2z" fill="#fff"/></svg>
    </div>
    <p>24815 Harrowgate Lane<br>Noblesville, IN 46062<br>317.555.0143</p>
  </div>
  <div class="location location--fishers">
    <div class="location__icons">
      <svg viewBox="0 0 16 16"><path d="M8 1a5 5 0 0 0-5 5c0 4 5 9 5 9s5-5 5-9a5 5 0 0 0-5-5z" fill="var(--crimson)"/><circle cx="8" cy="6" r="2" fill="#fff"/></svg>
      <svg viewBox="0 0 16 16"><circle cx="8" cy="8" r="8" fill="var(--crimson)"/><path d="M5 4l2 2-1 1.2c.6 1.2 1.6 2.2 2.8 2.8L10 9l2 2-1.2 1.4C7.5 12 4 8.5 3.6 5.2z" fill="#fff"/></svg>
    </div>
    <p>16250 Quillon Meadow Drive<br>Fishers, IN 46038<br>317-555-0178</p>
  </div>
</main>
</body>
</html>
```